I need a business card design for a real estate finance, development and management business. We deal with high net worth clients and ask that the business card be neat, clean and sophisticated. We like the attached logo design, font and color and want to incorporate all this into the business card.

Industry/Entity Type

Real Estate

```html
<!DOCTYPE html>
<html lang="en">
<head>
<meta charset="utf-8">
<title>Silver Harbor – Business Card</title>
<link rel="stylesheet" href="https://fonts.googleapis.com/css2?family=Cinzel:wght@400&family=Arimo:wght@400&display=swap">
<style>
  :root {
    --backdrop: #3a3a3a;
    --card: #050505;
    --brand-blue: #0b73b5;
    --tagline-grey: #b9b9b9;
    --rule-blue: #0b73b5;
  }
  * { box-sizing: border-box; margin: 0; padding: 0; }
  html, body {
    width: 1200px; height: 847px; overflow: hidden;
    background: var(--backdrop);
  }
  .sheet {
    width: 1200px; height: 847px;
    display: flex; align-items: center; justify-content: center; gap: 80px;
  }
  .card {
    position: relative;
    width: 490px; height: 280px;
    background: var(--card);
    border-radius: 22px;
    overflow: hidden;
  }
  .rule {
    position: absolute; height: 2px; background: var(--rule-blue);
  }
  .company-name {
    font-family: "Arimo", sans-serif;
    font-weight: 400;
    color: var(--brand-blue);
    white-space: nowrap;
  }
  .tagline {
    font-family: "Arimo", sans-serif;
    font-size: 10px;
    letter-spacing: 2.5px;
    text-transform: uppercase;
    white-space: nowrap;
  }

  /* Front */
  .card-front .company-name {
    position: absolute; left: 0; right: 0; top: 104px;
    text-align: center; font-size: 40px;
  }
  .card-front .tagline {
    position: absolute; left: 0; right: 0; top: 170px;
    text-align: center; color: var(--tagline-grey);
  }

  /* Back */
  .card-back .company-name {
    position: absolute; left: 26px; top: 24px; font-size: 36px;
  }
  .card-back .tagline {
    position: absolute; left: 28px; top: 76px; color: var(--brand-blue);
  }
  .card-back .rule-bottom { left: 0; right: 0; top: 250px; }
  .holder {
    position: absolute; left: 26px; top: 130px;
  }
  .holder-name {
    font-family: "Cinzel", serif; font-size: 24px; color: var(--brand-blue);
  }
  .holder-title {
    font-family: "Cinzel", serif; font-size: 11px; color: var(--brand-blue);
    letter-spacing: 1px; margin-top: 2px; margin-left: 26px;
  }
  .divider {
    position: absolute; left: 206px; top: 120px; width: 2px; height: 116px;
    background: var(--rule-blue);
  }
  .contacts {
    position: absolute; left: 218px; top: 122px;
    list-style: none;
  }
  .contacts li {
    display: flex; align-items: center; gap: 9px;
    height: 27px;
    font-family: "Cinzel", serif; font-size: 13px; color: var(--brand-blue);
    white-space: nowrap;
  }
  .contacts svg { width: 15px; height: 15px; flex: none; }
</style>
</head>
<body>
<main class="sheet">

  <section class="card card-front" aria-label="Card front">
    <div class="company-name">Silver Harbor</div>
    <div class="tagline">Capital &nbsp;Development &nbsp;Management</div>
  </section>

  <section class="card card-back" aria-label="Card back">
    <div class="company-name">Silver Harbor</div>
    <div class="tagline">Capital &nbsp;Development &nbsp;Management</div>

    <div class="holder">
      <div class="holder-name">Daniel Reed</div>
      <div class="holder-title">Administrator</div>
    </div>

    <div class="divider"></div>

    <ul class="contacts">
      <li>
        <svg viewBox="0 0 16 16" aria-hidden="true"><rect x="4" y="1" width="8" height="14" rx="1.5" fill="none" stroke="#0b73b5" stroke-width="1.4"/><line x1="7" y1="12.5" x2="9" y2="12.5" stroke="#0b73b5" stroke-width="1.4"/></svg>
        (555) 010-2040
      </li>
      <li>
        <svg viewBox="0 0 16 16" aria-hidden="true"><circle cx="8" cy="8" r="7.5" fill="#0b73b5"/><path d="M5.5 4.5 L7 4.5 L7.5 6.5 L6.6 7.2 Q7.5 9 9 9.6 L9.7 8.7 L11.5 9.2 L11.5 10.7 Q8 11.2 5.2 7.5 Q4.8 5.5 5.5 4.5Z" fill="#050505"/></svg>
        1-555-010-2041
      </li>
      <li>
        <svg viewBox="0 0 16 16" aria-hidden="true"><circle cx="8" cy="8" r="7" fill="none" stroke="#0b73b5" stroke-width="1.4"/><ellipse cx="8" cy="8" rx="3" ry="7" fill="none" stroke="#0b73b5" stroke-width="1.2"/><line x1="1" y1="8" x2="15" y2="8" stroke="#0b73b5" stroke-width="1.2"/></svg>
        www.silverharbor.example
      </li>
      <li>
        <svg viewBox="0 0 16 16" aria-hidden="true"><circle cx="8" cy="8" r="7.5" fill="#0b73b5"/><circle cx="8" cy="8" r="2.3" fill="none" stroke="#050505" stroke-width="1.4"/><path d="M10.3 6 L10.3 9 Q10.3 10.5 11.6 10.2 Q12.6 9.8 12.4 7.6 A4.5 4.5 0 1 0 10 12" fill="none" stroke="#050505" stroke-width="1.3"/></svg>
        d.reed@silverharbor.example
      </li>
    </ul>

    <div class="rule rule-bottom"></div>
  </section>

</main>
</body>
</html>
```